Smartwatch design for elderly and young people with disabilities

We are a small company offering mobile social care alarms to care givers and consumers in Europe. We will introduce our first social care alarm that are built upon a smart watch and want to by inspired how to design the screen interfaces.

We want to start with a competition of five different screen interfaces and five symbols within this project and to develop further with the chosen developer. See the different symbols and screens in the enclosed file.

Main focus; how shall a clock interface look like on a smartwatch for elderly, both the digital and the analog dial one? We see three main target groups.
1. Active seniors, that for any reason feel unsafe but want to stay active and live independently
2. Active seniors, who are affected by the syndromes of being early in the dementia disease or similar
3. Kids (age 7-12) with Down syndrome or autism that want to be active both indoors and outside

it is important that the user easily can see what time it is, but they and the relatives must also be able to see how much battery is left on the watch, the signal strength towards the mobile network. Target group 1 and 3 may want to see how many steps they have taken during the day. Our logo should be visible on the screen as well, but just in a small size. See the different symbols and screens we want you the draw in the enclosed file, Design startpoint .

The watch has an alarm button on the side of the watch to initiate alarms, it shall not be possible to do on the screen.
The screen size is 240x240 pixels, 43x43 mm
We want the the designs in gif-format.
Updates

Need extra days to review

Target Market(s)

Vulnerable people in the society that are offered support from caregivers

Industry/Entity Type

Consumer market and social care for elderly and young persons with cognitive disabilities

Font styles to use
Sans Serif

Requirements
Must have
• It's important that the user clearly can understand what time it is even if they have dementia or some kind of cognitive disability that can make it harder to understand. Suggestions of the different screens and symbols that we need.
Nice to have
• We haven't filled in colours and look and feel, because we we need both a more playful version for young persons and a more elegant version for elderly. The watch and the interfaces shall inspire to be more active outside their home, to give them a sense of freedom and to motivate them to be active where ever they want to be
Should not have
• Extra design elements that add nothing

```html
<!DOCTYPE html>
<html lang="en">
<head>
<meta charset="utf-8">
<title>Velora – senior watch screens concepts</title>
<link rel="stylesheet" href="https://fonts.googleapis.com/css2?family=Open+Sans:ital,wght@0,400;0,600;0,700;1,400;1,700&display=swap">
<style>
  :root {
    --bg: #000000;
    --ink: #ffffff;
    --caption: #c8c8c8;
    --rim: #3a3a3a;
  }
  * { margin: 0; padding: 0; box-sizing: border-box; }
  html, body { width: 720px; height: 1200px; overflow: hidden; background: var(--bg); }
  body { position: relative; font-family: "Open Sans", Arial, sans-serif; color: var(--ink); }

  .page-header { position: absolute; left: 18px; top: 17px; display: flex; align-items: baseline; gap: 7px; }
  .brand-name { font-size: 14px; font-weight: 600; color: var(--ink); }
  .header-title { font-size: 8px; color: var(--ink); }

  .screen { position: absolute; width: 100px; height: 100px; margin: -50px 0 0 -50px; }
  .screen svg { display: block; width: 100%; height: 100%; }
  .screen text { font-family: "Open Sans", Arial, sans-serif; fill: var(--ink); }

  .caption { position: absolute; left: 0; width: 720px; text-align: center; font-size: 8px; line-height: 16px; color: var(--caption); letter-spacing: 0.2px; }
  .caption b { font-style: italic; font-weight: 700; }
  .caption .note { font-style: italic; }
</style>
</head>
<body>

<header class="page-header">
  <span class="brand-name">Velora</span>
  <span class="header-title">senior watch screens concepts</span>
</header>

<!-- Main dials -->
<div class="screen screen--digital" style="left:232px; top:196px;">
  <svg viewBox="0 0 200 200">
    <defs>
      <linearGradient id="g-digital" x1="1" y1="0" x2="0" y2="1">
        <stop offset="0" stop-color="#d2a84c"/><stop offset="0.5" stop-color="#8a7a55"/><stop offset="1" stop-color="#1f3a55"/>
      </linearGradient>
    </defs>
    <circle cx="100" cy="100" r="98" fill="url(#g-digital)" stroke="var(--rim)" stroke-width="3"/>
    <g class="steps-icon" fill="#fff">
      <ellipse cx="92" cy="33" rx="8" ry="4"/><ellipse cx="92" cy="40" rx="7" ry="2.5"/>
      <ellipse cx="120" cy="42" rx="12" ry="7"/><ellipse cx="119" cy="55" rx="10" ry="5"/>
    </g>
    <text x="82" y="60" font-size="15" text-anchor="middle">7.234</text>
    <text x="100" y="124" font-size="58" text-anchor="middle">10:24</text>
    <rect x="54" y="140" width="36" height="17" rx="3" fill="#bbb"/>
    <rect x="54" y="140" width="15" height="17" rx="3" fill="#fff"/>
    <rect x="91" y="145" width="2" height="7" fill="#bbb"/>
    <g class="signal" fill="#fff">
      <rect x="108" y="153" width="4" height="4"/><rect x="114" y="150" width="4" height="7"/>
      <rect x="120" y="147" width="4" height="10"/><rect x="126" y="144" width="4" height="13" opacity="0.5"/>
      <rect x="132" y="141" width="4" height="16" opacity="0.5"/>
    </g>
    <text x="100" y="184" font-size="13" text-anchor="middle">Velora</text>
  </svg>
</div>

<div class="screen screen--analog" style="left:485px; top:196px;">
  <svg viewBox="0 0 200 200">
    <defs>
      <linearGradient id="g-analog" x1="0.8" y1="0" x2="0.2" y2="1">
        <stop offset="0" stop-color="#b7b55a"/><stop offset="0.55" stop-color="#7b9a3c"/><stop offset="1" stop-color="#2c6a2a"/>
      </linearGradient>
    </defs>
    <circle cx="100" cy="100" r="98" fill="url(#g-analog)" stroke="var(--rim)" stroke-width="3"/>
    <circle cx="100" cy="100" r="92" fill="none" stroke="#fff" stroke-width="6" stroke-dasharray="1 8.63"/>
    <circle cx="100" cy="100" r="91" fill="none" stroke="#fff" stroke-width="8" stroke-dasharray="3 44.65" transform="rotate(-90.9 100 100)"/>
    <g font-size="18" text-anchor="middle">
      <text x="100" y="35">12</text><text x="135" y="44">1</text><text x="163" y="68">2</text>
      <text x="172" y="107">3</text><text x="163" y="146">4</text><text x="135" y="172">5</text>
      <text x="100" y="180">6</text><text x="65" y="172">7</text><text x="37" y="146">8</text>
      <text x="28" y="107">9</text><text x="37" y="68">10</text><text x="65" y="44">11</text>
    </g>
    <text x="100" y="63" font-size="12" text-anchor="middle">Velora</text>
    <rect x="44" y="93" width="30" height="15" rx="2" fill="#bbb"/>
    <rect x="44" y="93" width="13" height="15" rx="2" fill="#fff"/>
    <g fill="#fff">
      <rect x="124" y="101" width="3" height="3"/><rect x="129" y="99" width="3" height="5"/>
      <rect x="134" y="97" width="3" height="7"/><rect x="139" y="94" width="3" height="10" opacity="0.5"/>
      <rect x="144" y="91" width="3" height="13" opacity="0.5"/>
    </g>
    <g fill="#fff">
      <ellipse cx="98" cy="120" rx="7" ry="3.5"/><ellipse cx="98" cy="126" rx="6" ry="2"/>
      <ellipse cx="125" cy="128" rx="11" ry="6"/><ellipse cx="124" cy="140" rx="9" ry="4.5"/>
    </g>
    <text x="84" y="148" font-size="15" text-anchor="middle">17.208</text>
    <line x1="100" y1="100" x2="54" y2="72" stroke="#fff" stroke-width="4" stroke-linecap="round"/>
    <line x1="100" y1="100" x2="168" y2="128" stroke="#fff" stroke-width="3" stroke-linecap="round"/>
    <line x1="100" y1="100" x2="156" y2="34" stroke="#a8d8f0" stroke-width="3" stroke-linecap="round"/>
    <circle cx="100" cy="100" r="4" fill="#fff"/>
  </svg>
</div>

<p class="caption" style="top:267px;">Main screen for <b>digital</b> and <b>analog</b> dials.</p>

<!-- Status alerts -->
<div class="screen screen--signal" style="left:232px; top:463px;">
  <svg viewBox="0 0 200 200">
    <defs>
      <linearGradient id="g-signal" x1="0.7" y1="0" x2="0.2" y2="1">
        <stop offset="0" stop-color="#d96a30"/><stop offset="0.6" stop-color="#b55a2e"/><stop offset="1" stop-color="#2f3a30"/>
      </linearGradient>
    </defs>
    <circle cx="100" cy="100" r="98" fill="url(#g-signal)" stroke="var(--rim)" stroke-width="3"/>
    <g fill="#e88e68" stroke="#f3b79b" stroke-width="1">
      <rect x="72" y="90" width="16" height="18"/><rect x="94" y="78" width="16" height="30"/>
      <rect x="116" y="66" width="16" height="42"/><rect x="138" y="54" width="16" height="54"/>
    </g>
    <polygon points="50,108 66,108 66,98" fill="#fff"/>
    <text x="100" y="152" font-size="20" text-anchor="middle">Bad signal!</text>
    <text x="100" y="184" font-size="13" text-anchor="middle">Velora</text>
  </svg>
</div>

<div class="screen screen--battery" style="left:485px; top:463px;">
  <svg viewBox="0 0 200 200">
    <defs>
      <linearGradient id="g-battery" x1="0" y1="0.2" x2="1" y2="0.9">
        <stop offset="0" stop-color="#d8201e"/><stop offset="0.6" stop-color="#c84a2a"/><stop offset="1" stop-color="#9a8a30"/>
      </linearGradient>
    </defs>
    <circle cx="100" cy="100" r="98" fill="url(#g-battery)" stroke="var(--rim)" stroke-width="3"/>
    <rect x="92" y="15" width="16" height="3" fill="#fff"/>
    <rect x="75" y="20" width="50" height="96" rx="7" fill="#ec7b78"/>
    <path d="M75 94 H125 V109 a7 7 0 0 1 -7 7 H82 a7 7 0 0 1 -7 -7 Z" fill="#fff"/>
    <text x="100" y="152" font-size="20" text-anchor="middle">Charge battery!</text>
    <text x="100" y="184" font-size="13" text-anchor="middle">Velora</text>
  </svg>
</div>

<p class="caption" style="top:544px;">Alert message screens for <b>Bad signal</b> and <b>Low battery</b>.<br>
<span class="note">Sound, vibration, icons, and background colour should grab user attention.</span></p>

<!-- Alarm -->
<div class="screen screen--alarm" style="left:360px; top:710px;">
  <svg viewBox="0 0 200 200">
    <defs>
      <linearGradient id="g-alarm" x1="0.8" y1="0" x2="0.2" y2="1">
        <stop offset="0" stop-color="#c9a050"/><stop offset="0.45" stop-color="#d84ad0"/><stop offset="1" stop-color="#5a2aa0"/>
      </linearGradient>
    </defs>
    <circle cx="100" cy="100" r="98" fill="url(#g-alarm)" stroke="var(--rim)" stroke-width="3"/>
    <g fill="#fff">
      <path d="M100 38 c-20 0 -30 16 -30 34 v14 l-8 14 h76 l-8 -14 v-14 c0 -18 -10 -34 -30 -34 Z"/>
      <circle cx="100" cy="36" r="4"/>
      <path d="M90 104 a10 8 0 0 0 20 0 Z"/>
    </g>
    <g fill="none" stroke="#fff" stroke-width="4" stroke-linecap="round">
      <path d="M66 46 q-8 10 -7 24"/><path d="M134 46 q8 10 7 24"/>
    </g>
    <text x="100" y="152" font-size="20" text-anchor="middle">Alarm initiated!</text>
    <text x="100" y="184" font-size="13" text-anchor="middle">Velora</text>
  </svg>
</div>

<p class="caption" style="top:791px;">Alert message screen for <b>Alarm initiated</b>.<br>
<span class="note">Some alert notifications appear only in certain situation, so for example alarm will work at specific time it set to.</span><br>
<span class="note">If use only screen to place all the information it would be very cluttered and hard to read.</span></p>

<!-- Reminders -->
<div class="screen screen--walk" style="left:232px; top:980px;">
  <svg viewBox="0 0 200 200">
    <defs>
      <linearGradient id="g-walk" x1="0.9" y1="0" x2="0.1" y2="1">
        <stop offset="0" stop-color="#c8b860"/><stop offset="0.45" stop-color="#2fa8a0"/><stop offset="1" stop-color="#1a3a6a"/>
      </linearGradient>
    </defs>
    <circle cx="100" cy="100" r="98" fill="url(#g-walk)" stroke="var(--rim)" stroke-width="3"/>
    <g fill="#fff">
      <ellipse cx="108" cy="34" rx="13" ry="5"/><ellipse cx="108" cy="44" rx="11" ry="3"/>
      <ellipse cx="69" cy="56" rx="18" ry="7"/><ellipse cx="70" cy="71" rx="15" ry="5"/>
      <ellipse cx="122" cy="84" rx="26" ry="14"/><ellipse cx="122" cy="110" rx="21" ry="9"/>
    </g>
    <text x="100" y="152" font-size="20" text-anchor="middle">Take a walk!</text>
    <text x="100" y="184" font-size="13" text-anchor="middle">Velora</text>
  </svg>
</div>

<div class="screen screen--medicine" style="left:485px; top:980px;">
  <svg viewBox="0 0 200 200">
    <defs>
      <linearGradient id="g-medicine" x1="0.9" y1="0.1" x2="0.1" y2="0.9">
        <stop offset="0" stop-color="#7ad0c8"/><stop offset="0.5" stop-color="#3f6ed0"/><stop offset="1" stop-color="#4a2a90"/>
      </linearGradient>
    </defs>
    <circle cx="100" cy="100" r="98" fill="url(#g-medicine)" stroke="var(--rim)" stroke-width="3"/>
    <rect x="102" y="38" width="44" height="20" rx="10" fill="#fff"/>
    <path d="M56 56 q0 -10 12 -12 l28 -4" fill="none" stroke="#fff" stroke-width="4" stroke-linecap="round"/>
    <path d="M54 96 a22 22 0 0 1 44 0 Z M54 102 h44 a22 22 0 0 1 -44 0 Z" fill="#fff"/>
    <circle cx="124" cy="98" r="23" fill="#fff"/>
    <line x1="109" y1="82" x2="139" y2="114" stroke="#3f6ed0" stroke-width="4"/>
    <text x="100" y="152" font-size="20" text-anchor="middle">Medicine time!</text>
    <text x="100" y="184" font-size="13" text-anchor="middle">Velora</text>
  </svg>
</div>

<p class="caption" style="top:1061px;">Alert message screens for <b>Take a walk</b> and <b>Take your medicine</b>.<br>
<span class="note">Thus using alert notifications screens instead of placing specific indications on the main screen</span><br>
<span class="note">will allow for less cluttered main screen and better focus on the alert messages.</span></p>

</body>
</html>
```